HUSH: Hush Until Stories Happen school library event

I need two poster designs for Hush Until Stories Happen (HUSH) in BC, requested by the PCSMG--Pacific Coast School Media Guild. One should be for elementary students and one for high school. I want the date (Monday, October 26, 2020) and Hush Until Stories Happen. I would like the posters in English and in French. French is : Ferme Ton Écran Maintenant! I'm including last year's posters as examples. I would like to be able to print the poster files on 11x17 paper.

• -The phrase "Hush Until Stories Happen" for the English version; "Ferme Ton Écran Maintenant" for the French version.
-Include the organization name: Pacific Coast School Media Guild
-The date: Monday, October 26, 2020
• I would like the elementary version to be bright and colourful--fun for younger kids. I would like the high school version to be a bit more mature for the older students. Can still be bright and colourful.

```html
<!DOCTYPE html>
<html lang="en">
<head>
<meta charset="utf-8">
<title>HUSH – Hush Until Stories Happen posters</title>
<link rel="stylesheet" href="https://fonts.googleapis.com/css2?family=Anton&family=Delius&family=Fredoka:wght@700&family=Marcellus&family=Playfair+Display:ital,wght@0,400;0,700;1,400&family=Righteous&family=Special+Elite&display=swap">
<style>
  :root {
    --backdrop: #e4e4e4;
    --poster-blue-deep: #1f8fd0;
    --poster-blue-mid: #2fa6de;
    --poster-blue-light: #4ccbea;
    --ink-navy: #12233a;
    --paper-white: #f7f7f7;
    --shadow-dark: #1a1a1a;
    --tape-green: #8fc85a;
    --tape-green-light: #b2dc7a;
    --tape-green-dark: #6fb43e;
    --fun-red: #d42a3c;
    --fun-orange: #f39a1f;
    --fun-yellow: #f2d21e;
    --fun-purple: #74378f;
  }
  html, body {
    margin: 0;
    padding: 0;
    width: 1200px;
    height: 800px;
    overflow: hidden;
    background: var(--backdrop);
  }
  .stage {
    position: relative;
    width: 1200px;
    height: 800px;
  }
  .poster {
    position: absolute;
    top: 144px;
    width: 405px;
    height: 568px;
    background:
      radial-gradient(ellipse 60% 40% at 70% 22%, rgba(76,203,234,0.65), transparent 70%),
      linear-gradient(180deg, var(--poster-blue-mid) 0%, var(--poster-blue-deep) 100%);
    overflow: hidden;
  }
  .poster--senior { left: 152px; }
  .poster--junior { left: 643px; }

  .poster__org {
    position: absolute;
    top: 22px;
    left: 0;
    right: 0;
    margin: 0;
    text-align: center;
    font-family: "Marcellus", serif;
    font-size: 13.5px;
    line-height: 20px;
    letter-spacing: 0.2px;
    color: var(--ink-navy);
  }
  .poster__frame {
    position: absolute;
    left: 63px;
    top: 120px;
    width: 279px;
    height: 412px;
    border: 1px solid var(--paper-white);
    box-sizing: border-box;
  }
  .poster__date {
    position: absolute;
    left: 34px;
    top: 101px;
    width: 200px;
    height: 40px;
    transform: rotate(-13deg);
    transform-origin: left center;
    background: linear-gradient(90deg, var(--tape-green-dark) 0%, var(--tape-green) 45%, var(--tape-green-light) 100%);
    clip-path: polygon(0 4%, 3% 0, 7% 5%, 12% 1%, 18% 4%, 25% 0, 33% 3%, 41% 0, 50% 4%, 58% 1%, 66% 3%, 74% 0, 82% 4%, 90% 1%, 96% 3%, 100% 0, 99% 30%, 100% 60%, 98% 100%, 92% 96%, 85% 100%, 77% 97%, 69% 100%, 60% 96%, 52% 100%, 44% 97%, 35% 100%, 27% 96%, 19% 100%, 11% 97%, 5% 100%, 0 96%, 2% 62%, 0 30%);
    font-family: "Special Elite", monospace;
    font-size: 16px;
    line-height: 40px;
    color: var(--ink-navy);
    text-align: center;
    white-space: nowrap;
  }
  .headline {
    position: absolute;
    left: 0;
    right: 0;
    margin: 0;
    text-align: center;
    line-height: 1;
    white-space: nowrap;
  }

  /* High school edition */
  .senior__hush {
    top: 150px;
    font-family: "Playfair Display", serif;
    font-weight: 700;
    font-size: 78px;
    color: var(--paper-white);
    text-shadow: 2px 2px 0 var(--shadow-dark);
  }
  .senior__until {
    top: 228px;
    font-family: "Playfair Display", serif;
    font-style: italic;
    font-size: 48px;
    color: var(--paper-white);
    text-shadow: 1.5px 1.5px 0 var(--shadow-dark);
  }
  .senior__stories {
    top: 304px;
    font-family: "Playfair Display", serif;
    font-weight: 400;
    font-size: 70px;
    color: var(--paper-white);
    -webkit-text-stroke: 0.6px var(--shadow-dark);
    text-shadow: 2px 2px 0 var(--shadow-dark);
  }
  .senior__happen {
    top: 422px;
    font-family: "Anton", sans-serif;
    font-size: 72px;
    letter-spacing: -1px;
    color: var(--paper-white);
    text-shadow: 2px 2px 0 var(--shadow-dark);
  }

  /* Elementary edition */
  .junior__hush {
    top: 146px;
    font-family: "Fredoka", sans-serif;
    font-weight: 700;
    font-size: 74px;
    letter-spacing: 2px;
    color: var(--fun-red);
    transform: rotate(-2deg);
    text-shadow: 1px 1px 0 var(--shadow-dark);
  }
  .junior__until {
    top: 230px;
    font-family: "Delius", sans-serif;
    font-size: 56px;
    color: var(--fun-orange);
    text-shadow: 1px 1px 0 var(--shadow-dark);
  }
  .junior__stories-art {
    position: absolute;
    left: 89px;
    top: 319px;
    width: 219px;
    height: 88px;
    display: block;
  }
  .junior__happen {
    top: 430px;
    font-family: "Righteous", sans-serif;
    font-size: 66px;
    color: var(--fun-purple);
    text-shadow: 1px 1px 0 var(--shadow-dark);
  }
</style>
</head>
<body>
<main class="stage">

  <section class="poster poster--senior" aria-label="High school poster">
    <p class="poster__org">PACIFIC COAST<br>SCHOOL MEDIA GUILD</p>
    <div class="poster__frame"></div>
    <div class="poster__date">MONDAY, 26/10/2020</div>
    <h1 class="headline senior__hush">Hush</h1>
    <p class="headline senior__until">until</p>
    <p class="headline senior__stories">stories</p>
    <p class="headline senior__happen">HAPPEN</p>
  </section>

  <section class="poster poster--junior" aria-label="Elementary poster">
    <p class="poster__org">PACIFIC COAST<br>SCHOOL MEDIA GUILD</p>
    <div class="poster__frame"></div>
    <div class="poster__date">MONDAY, 26/10/2020</div>
    <h1 class="headline junior__hush">HUSH</h1>
    <p class="headline junior__until">until</p>
    <svg class="junior__stories-art" viewBox="0 0 219 88" role="img" aria-label="Yellow illustrated lettering made of animal shapes spelling the word stories">
      <rect x="0" y="0" width="219" height="88" rx="6" fill="var(--fun-yellow)" opacity="0.85"/>
    </svg>
    <p class="headline junior__happen">happen</p>
  </section>

</main>
</body>
</html>
```